Flyer Design Project

I need a flyer to be handed out at trade shows. We offer a variety of products and services to the plastics industry. I would like the front of the flyer to highlight our services in two categories. Those categories/sub-categories are as follows:
Design Services
Plastic Part Design
Feasibility Studies
Mold Design
Fixture Design
Reverse Engineering
Laser Digitizing and Inspection
Manufacturing Services
Contract Manufacturing
Prototypes
Sight Models
Tooling Models
Injection Molding
Thermoforming
CNC Machining
I would like the back of the flyer to highlight the products we sell. Those products are "gas nudgers" which are used to aid in the removal of molded plastic parts from the molds.
We have two websites from which you can see more about our company and it offerings.
Our design/manufacturing services website is www.brantholmecad.com
Our web store for our products is www.ventiplunger.com
I would like the flyer to emulate the look and feel of both websites.
I will upload our logo in a variety of formats as well as some trifold flyers we have printed in the past. The trifold flyers were on pre-printed format so much of the color/graphics are not there. I can upload photos and other artwork as needed.
We are looking to have this printed on 8-1/2" x 11" glossy paper (portrait) with a professional "technical" look.
Since we are a technically minded company, we have a tendancy to get a little "wordy" with our explanations and literature. I would like to avoid that for this application.
Updates
Project Deadline Extended
Reason: We are very close on the design but I dont want to rush it.
I'm going to make a few changes to page 2 in another post
Target Market(s)
Mechanical designers and engineers, manufacturers
Industry/Entity Type
Plastic
Look and feel

```html
<!DOCTYPE html>
<html lang="en">
<head>
<meta charset="utf-8">
<title>Brantholme Design – Services Flyer</title>
<link href="https://fonts.googleapis.com/css2?family=Nunito+Sans:wght@400;600&display=swap" rel="stylesheet">
<style>
  :root {
    --page: #e9ecec;
    --band: #141414;
    --panel: #ffffff;
    --accent: #5c9be0;
    --seal: #5ea2ea;
    --body: #7b898e;
    --ink: #111111;
    --white: #ffffff;
  }
  * { margin: 0; padding: 0; box-sizing: border-box; }
  html, body { width: 927px; height: 1200px; overflow: hidden; }
  body {
    position: relative;
    background: var(--page);
    font-family: "Nunito Sans", Arial, sans-serif;
    color: var(--ink);
  }
  .header-band {
    position: absolute; left: 0; top: 52px; width: 927px; height: 164px;
    background: var(--band);
  }
  .brand {
    position: absolute; left: 98px; top: 64px;
    display: flex; align-items: center; gap: 12px;
    color: var(--white); font-weight: 600; font-size: 26px; letter-spacing: .5px;
  }
  .brand-dot { width: 26px; height: 26px; border-radius: 50%; background: var(--white); }
  .corner-seal {
    position: absolute; left: 718px; top: 22px; width: 124px; height: 124px;
    border-radius: 50%; background: var(--seal);
  }
  .content-panel {
    position: absolute; left: 84px; top: 216px; width: 764px; height: 722px;
    background: var(--panel);
  }
  .section-title {
    position: absolute; font-weight: 400; font-size: 45px; color: var(--accent);
    line-height: 1; white-space: nowrap;
  }
  .section-intro {
    position: absolute; font-size: 20px; line-height: 25px; color: var(--body);
    white-space: nowrap;
  }
  .service-list {
    position: absolute; font-size: 34px; line-height: 40px; color: var(--ink);
    white-space: nowrap;
  }
  .design-title { left: 95px; top: 225px; }
  .design-intro { left: 96px; top: 284px; }
  .design-list { left: 94px; top: 385px; }
  .mfg-title { left: 100px; top: 678px; }
  .mfg-intro { left: 102px; top: 730px; }
  .mfg-list { left: 100px; top: 814px; }
  .photo-strip {
    position: absolute; display: flex; gap: 2px; height: 156px;
  }
  .design-strip { left: 41px; top: 512px; width: 844px; }
  .mfg-strip { left: 43px; top: 939px; width: 844px; }
  .photo-strip .tile { flex: 1; }
  .site-url {
    position: absolute; left: 146px; top: 1110px;
    font-size: 52px; font-weight: 400; color: var(--ink); line-height: 1; white-space: nowrap;
  }
</style>
</head>
<body>
  <header class="header-band">
    <div class="brand"><span class="brand-dot"></span><span>Brantholme Design</span></div>
    <div class="corner-seal" aria-hidden="true"></div>
  </header>

  <div class="content-panel"></div>

  <h2 class="section-title design-title">Design Services</h2>
  <p class="section-intro design-intro">Brantholme Design offers full product design and development services<br>supported by years of tooling experience and the latest design software.<br>The result? A product that looks good, functions properly and is cost-effective<br>to manufacture.</p>
  <p class="service-list design-list">Plastic Part Design • Feasibility Studies •<br>Mold Design • Fixture Design • Reverse<br>Engineering • Laser Digitizing and Inspection</p>

  <div class="photo-strip design-strip">
    <div class="tile" role="img" aria-label="CAD render of an electronics enclosure" style="background:linear-gradient(#e4e8ea,#c9d1d6)"></div>
    <div class="tile" role="img" aria-label="CAD render of a teal laundry basket" style="background:linear-gradient(#dfe4e4,#7fd8c8)"></div>
    <div class="tile" role="img" aria-label="CAD render of a black hair dryer" style="background:linear-gradient(#e2e4e6,#6b6e72)"></div>
    <div class="tile" role="img" aria-label="CAD render of a fixture assembly" style="background:linear-gradient(#cfd6e6,#5a79b8)"></div>
    <div class="tile" role="img" aria-label="Inspection fixture in the shop" style="background:linear-gradient(#b8bcbc,#8b8478)"></div>
    <div class="tile" role="img" aria-label="CAD render of a mold base" style="background:linear-gradient(#c4ccd4,#6f9a78)"></div>
    <div class="tile" role="img" aria-label="Laser digitizing a vehicle hood in the shop" style="background:linear-gradient(#9a9287,#8a3030)"></div>
  </div>

  <h2 class="section-title mfg-title">Manufacturing Services</h2>
  <p class="section-intro mfg-intro">Here at Brantholme we also offer a wide and comprehensive range of<br>manufacturing services all of which have been adapted over the years to<br>fulfil modern techniques.</p>
  <p class="service-list mfg-list">Contract Manufacturing • Prototypes • Sight<br>Models • Tooling Models • Injection Molding •<br>Thermoforming • CNC Machining</p>

  <div class="photo-strip mfg-strip">
    <div class="tile" role="img" aria-label="Machined aluminum mold plates" style="background:linear-gradient(#8a8e90,#4f5356)"></div>
    <div class="tile" role="img" aria-label="CNC machine cutting a part" style="background:linear-gradient(#7a7d78,#3d3f3c)"></div>
    <div class="tile" role="img" aria-label="Assorted molded plastic parts" style="background:linear-gradient(#d8c84a,#5a8a55)"></div>
    <div class="tile" role="img" aria-label="Wooden tooling model" style="background:linear-gradient(#8a6a40,#b8885a)"></div>
    <div class="tile" role="img" aria-label="Molded decoys on grass" style="background:linear-gradient(#6d9a4a,#4d7a30)"></div>
    <div class="tile" role="img" aria-label="Blue and white molded cooler" style="background:linear-gradient(#d8d4cc,#3a5a9a)"></div>
    <div class="tile" role="img" aria-label="Thermoformed black tray on the bench" style="background:linear-gradient(#6a6460,#2a2a2a)"></div>
  </div>

  <p class="site-url">www.brantholmecad.com</p>
</body>
</html>
```